Company profile urgent

Hi, I had my designer fail to deliver and I am looking for urgent designers job. Needs to go to print tomorrow the latest. I need company profile designed and finished, I do have a start of the project but did not like the overall design as it was too simple and not something I would asking for. This needs to be a great job and we are willing to pay for the right job.

This is pretty much a folded brochure as you will see from the document that is attached. On the front side do not remove LOGO from the actual position as it must stay there for the purposes of the cover that is going over and it has a whole for the logo where it is. Also, the pages are set as it should be so do not change the order of the pages, only the design, feel and look. This is for a travel company needs to look expensive, upscale, vip and must have clean design.

Needs to be done:

.

Needs to be done:

1) Get the design more attractive and modern. Not looking for cheap but high quality material.
2) As you can see we are tryin to present 4 products in the brochure that we do and this will be a folded brochure.
3) Infographics, especially the table ''when to travel'' needs updates and more style
4) This design is very steril, we are looking for clean and modern design
5) On the front page add Company profile text somewhere and add any design on home page is welcome BUT logo must stay where is
6) Please send final print ready documents as well as editable so we can move the logo if needed as it must fit the whole on a brochure holder
7) Last page with contacts very poorly done by my designer, needs upgrade with maybe infographics for phone, email web etc... ideas welcome
8) if you need more photos at the end is link to photo bank

Ideas welcome! Again we need it fast and clean.

Photo bank:
https://files.orvenbox.example/f/q7Lm2Xa9Tz4Pb8Kd

Designes that we linked: https://layoutmarket.example/item/company-profile-square-brochure/48817203?s_rank=8
https://layoutmarket.example/item/company-profile_square/51390628?s_rank=32
https://layoutmarket.example/item/square-brochure/53704916?s_rank=52

This is our webiste so you get the feeling of the colors: www.selvotrips.example

Important: Do not change text, or change pages, everything is as it should be just needs upgradede design! Logo on the first page must stay on the position as is.

Photo bank:

Target Market(s)

We are travel supplier targeting travel agents and travel companies

Industry/Entity Type

Travel Industry

Font styles to use
Serif
Sans Serif

Requirements
Must have
• https://files.orvenbox.example/f/w3Hn6Rc1Ys5Qe2Jv
Nice to have
• Cool design: https://layoutmarket.example/item/business-solution-brochure-template/46182057?s_rank=3
• Cool design 2: https://layoutmarket.example/item/travel-agency-catalog-brochure/47269815?s_rank=6
Should not have
• Do not change the dimensions. You have the design attached, indd file. Needs work and update.

```html
<!DOCTYPE html>
<html lang="en">
<head>
<meta charset="utf-8">
<title>Selvo Trips – Croatia Company Profile</title>
<link rel="stylesheet" href="https://fonts.googleapis.com/css2?family=Montserrat:wght@400;500;600;700;800&display=swap">
<style>
:root{
  --red:#a3101f;
  --red-deep:#8c0d1a;
  --red-tile:rgba(160,14,30,.88);
  --white:#ffffff;
  --backdrop:#dcdcdc;
  --sea:#2f7f8c;
  --sky:#c9cfd6;
}
*{box-sizing:border-box;margin:0;padding:0}
html,body{width:1200px;height:1200px;overflow:hidden}
body{background:var(--backdrop);font-family:"Montserrat",Arial,sans-serif;color:var(--white);position:relative}

/* ---------- Spread 1: country facts ---------- */
.spread-facts{position:absolute;left:30px;top:26px;width:1137px;height:568px;overflow:hidden;background:var(--white)}
.coast-photo{position:absolute;inset:0;background:
  linear-gradient(180deg,#dfe2e6 0%,#b9c0c9 22%,#7f8a78 45%,#5b6b4a 58%,#2f7f8c 75%,#1f6470 100%)}
.map-area{position:absolute;left:520px;top:0;width:617px;height:380px;
  background:radial-gradient(ellipse at 60% 40%,rgba(163,16,31,.92),rgba(140,13,26,.85) 60%,rgba(163,16,31,.55) 100%)}
.town-photo{position:absolute;left:700px;top:200px;width:437px;height:200px;
  background:linear-gradient(135deg,#c98a5a,#d9b48d 50%,#b96a3e);opacity:.55}
.map-pin{position:absolute;left:893px;top:92px}

.country-title{position:absolute;left:40px;top:62px;font-size:36px;font-weight:500;color:var(--red);letter-spacing:1px}
.title-rule{position:absolute;left:40px;top:106px;width:290px;height:3px;background:#3a1a1e}

.fact-tile{position:absolute;background:var(--red-tile);width:136px;height:138px;padding:8px}
.fact-tile .frame{border:1px solid rgba(255,255,255,.85);width:100%;height:100%;display:flex;flex-direction:column;align-items:center;justify-content:flex-end;padding-bottom:6px;text-align:center;overflow:hidden}
.fact-tile svg{margin-bottom:auto;margin-top:12px}
.fact-value{font-size:11px;font-weight:500;letter-spacing:.2px;padding:0 2px 3px;border-bottom:1px solid rgba(255,255,255,.8);width:92%;white-space:nowrap}
.fact-value.small{font-size:6.3px;line-height:1.35;letter-spacing:0}
.fact-value.parks{font-size:8.5px;line-height:1.3}
.fact-label{font-size:15px;font-weight:700;margin-top:4px;letter-spacing:.3px;white-space:nowrap}
.fact-label.small{font-size:11px}
.tile-airports .frame{position:relative}
.airport-list{position:absolute;left:58px;top:32px;font-size:8px;line-height:8.6px;text-align:left;font-weight:500;white-space:nowrap}
.airport-plane{position:absolute;left:12px;top:50px;margin:0!important}
.airport-label{position:absolute;left:0;right:0;bottom:10px}

.route-line{position:absolute;left:504px;top:505px;width:130px;border-top:2px dashed var(--red)}

.travel-table-panel{position:absolute;left:604px;top:368px;width:498px;height:200px;background:rgba(163,16,31,.93)}
.suitcase-badge{position:absolute;left:646px;top:350px;width:70px;height:70px;border:1.5px solid var(--white);border-radius:50%;background:var(--red);display:flex;align-items:center;justify-content:center}
.travel-table{position:absolute;left:632px;top:423px;border-collapse:collapse;font-size:9px}
.travel-table th,.travel-table td{border:1px solid rgba(255,255,255,.75);height:29px;text-align:center;font-weight:500}
.travel-table thead th{border-top:none;height:24px}
.travel-table th.corner{border:none;text-align:left;font-weight:700;font-size:10.5px;width:100px;border-right:1px solid rgba(255,255,255,.75)}
.travel-table th.month{width:29px}
.travel-table th.row-label{text-align:left;font-size:11px;border-left:none;border-right:1px solid rgba(255,255,255,.75);padding-left:2px;white-space:nowrap}
.travel-table td svg{display:block;margin:auto}
.row-label span{display:inline-block;width:16px;height:16px;border:1px solid var(--white);border-radius:50%;vertical-align:middle;margin-right:4px}

/* ---------- Spread 2: agents & contact ---------- */
.spread-contact{position:absolute;left:25px;top:608px;width:1137px;height:568px;background:var(--white);overflow:hidden}
.agent-photo{position:absolute;left:0;top:0;width:568px;height:568px;
  background:linear-gradient(160deg,#c6d7de 0%,#b7cad2 40%,#d9dfe2 70%,#eef0f0 100%)}
.agent-box{position:absolute;left:0;top:338px;width:373px;height:204px;background:var(--red);padding:14px 0 0 33px}
.agent-box-tab{position:absolute;left:380px;top:338px;width:13px;height:13px;background:var(--red)}
.agent-title{font-size:13.5px;font-weight:700;line-height:21px;letter-spacing:.2px}
.agent-title .em{font-size:19px}
.agent-rule{width:340px;margin-left:-33px;border-top:1px solid rgba(255,255,255,.8);margin-top:3px;margin-bottom:12px}
.agent-points{list-style:none;font-size:11.5px;line-height:14.5px;font-weight:400}
.agent-points li::before{content:"• "}
.agent-close{margin-top:16px;font-size:11.5px;font-weight:600;line-height:14.5px}

.contact-page{position:absolute;left:568px;top:0;width:569px;height:568px;text-align:center;color:var(--red)}
.brand-mark{position:absolute;left:0;right:0;top:282px;display:flex;align-items:center;justify-content:center;gap:10px;font-size:34px;font-weight:800;letter-spacing:4px}
.brand-mark i{display:block;width:14px;height:14px;background:var(--red)}
.contact-lines{position:absolute;left:0;right:0;top:396px;font-size:14px;line-height:17.6px;font-weight:400}
.contact-lines strong{font-weight:700;display:block}
</style>
</head>
<body>

<svg width="0" height="0" style="position:absolute" aria-hidden="true">
  <symbol id="face-happy" viewBox="0 0 20 20"><circle cx="10" cy="10" r="8.5" fill="none" stroke="#fff" stroke-width="1.2"/><circle cx="7" cy="8" r="1" fill="#fff"/><circle cx="13" cy="8" r="1" fill="#fff"/><path d="M6 11.5q4 4 8 0" fill="none" stroke="#fff" stroke-width="1.2"/></symbol>
  <symbol id="face-neutral" viewBox="0 0 20 20"><circle cx="10" cy="10" r="8.5" fill="none" stroke="#fff" stroke-width="1.2"/><circle cx="7" cy="8" r="1" fill="#fff"/><circle cx="13" cy="8" r="1" fill="#fff"/><path d="M6.5 13h7" stroke="#fff" stroke-width="1.2"/></symbol>
  <symbol id="face-sad" viewBox="0 0 20 20"><circle cx="10" cy="10" r="8.5" fill="none" stroke="#fff" stroke-width="1.2"/><circle cx="7" cy="8" r="1" fill="#fff"/><circle cx="13" cy="8" r="1" fill="#fff"/><path d="M6 14.5q4 -4 8 0" fill="none" stroke="#fff" stroke-width="1.2"/></symbol>
</svg>

<section class="spread-facts">
  <div class="coast-photo" role="img" aria-label="Photo of a stone fortress on a green cliff above a turquoise sea under cloudy sky"></div>
  <div class="map-area" role="img" aria-label="Red-tinted map of Europe with Croatia highlighted"></div>
  <div class="town-photo" role="img" aria-label="Photo of an old town with orange tiled roofs"></div>
  <svg class="map-pin" width="40" height="62" viewBox="0 0 40 62" aria-hidden="true"><path d="M20 2a18 18 0 0 1 18 18c0 14-18 40-18 40S2 34 2 20A18 18 0 0 1 20 2z" fill="#fff"/><circle cx="20" cy="20" r="11" fill="#a3101f"/></svg>

  <h1 class="country-title">CROATIA</h1>
  <div class="title-rule"></div>

  <div class="fact-tile" style="left:42px;top:118px">
    <div class="frame">
      <svg width="80" height="66" viewBox="0 0 80 66" aria-hidden="true"><path d="M4 4h72v44H30l-14 14V48H4z" fill="none" stroke="#fff" stroke-width="3" stroke-linejoin="round"/><text x="40" y="31" fill="#fff" font-size="10" text-anchor="middle" font-family="Montserrat,sans-serif">CROATIAN</text></svg>
      <div class="fact-label">LANGUAGE</div>
    </div>
  </div>
  <div class="fact-tile" style="left:188px;top:118px">
    <div class="frame">
      <svg width="72" height="50" viewBox="0 0 72 50" aria-hidden="true"><g fill="#fff"><circle cx="8" cy="6" r="4"/><rect x="4" y="11" width="8" height="14" rx="2"/><circle cx="24" cy="6" r="4"/><rect x="20" y="11" width="8" height="14" rx="2"/><circle cx="40" cy="6" r="4"/><rect x="36" y="11" width="8" height="14" rx="2"/><circle cx="56" cy="6" r="4"/><rect x="52" y="11" width="8" height="14" rx="2"/><circle cx="16" cy="26" r="4"/><rect x="12" y="31" width="8" height="14" rx="2"/><circle cx="32" cy="26" r="4"/><rect x="28" y="31" width="8" height="14" rx="2"/><circle cx="48" cy="26" r="4"/><rect x="44" y="31" width="8" height="14" rx="2"/><circle cx="64" cy="26" r="4"/><rect x="60" y="31" width="8" height="14" rx="2"/></g></svg>
      <div class="fact-value">4.284 MILLION</div>
      <div class="fact-label">POPULATION</div>
    </div>
  </div>

  <div class="fact-tile" style="left:42px;top:262px">
    <div class="frame">
      <svg width="50" height="44" viewBox="0 0 50 44" aria-hidden="true"><g fill="none" stroke="#fff" stroke-width="2.5"><ellipse cx="18" cy="7" rx="14" ry="5"/><path d="M4 7v24c0 3 6 5 14 5"/><path d="M32 7v14"/><path d="M4 15c0 3 6 5 14 5M4 23c0 3 6 5 14 5"/><ellipse cx="34" cy="27" rx="12" ry="4"/><path d="M22 27v10c0 2 5 4 12 4s12-2 12-4V27"/></g></svg>
      <div class="fact-value">KUNA (HRK)</div>
      <div class="fact-label">CURRENCY</div>
    </div>
  </div>
  <div class="fact-tile" style="left:188px;top:262px">
    <div class="frame">
      <svg width="56" height="50" viewBox="0 0 56 50" aria-hidden="true"><g fill="none" stroke="#fff" stroke-width="2"><path d="M6 16L28 4l22 12z"/><path d="M10 20v20M19 20v20M28 20v20M37 20v20M46 20v20"/><path d="M4 44h48M2 48h52"/></g></svg>
      <div class="fact-value small">8 PROPERTIES INSCRIBED ON<br>THE WORLD HERITAGE LIST</div>
      <div class="fact-label">UNESCO</div>
    </div>
  </div>

  <div class="fact-tile" style="left:42px;top:406px">
    <div class="frame">
      <svg width="44" height="54" viewBox="0 0 44 54" aria-hidden="true"><g fill="none" stroke="#fff" stroke-width="2.4"><path d="M22 2v12M17 7h10"/><path d="M14 26l8-10 8 10v24H14z"/><path d="M4 34h10M30 34h10M4 34v16h36V34"/><path d="M19 50v-9h6v9"/></g></svg>
      <div class="fact-value">CATHOLIC</div>
      <div class="fact-label">RELIGION</div>
    </div>
  </div>
  <div class="fact-tile" style="left:188px;top:406px">
    <div class="frame">
      <svg width="58" height="54" viewBox="0 0 58 54" aria-hidden="true"><g fill="#fff"><circle cx="24" cy="14" r="12"/><circle cx="42" cy="22" r="8"/><rect x="22" y="22" width="4" height="16"/><rect x="40" y="28" width="3" height="10"/></g><g fill="none" stroke="#fff" stroke-width="2"><path d="M6 42q5-3 10 0t10 0 10 0 10 0 10 0M6 48q5-3 10 0t10 0 10 0 10 0 10 0"/></g></svg>
      <div class="fact-value parks">8 SPECTACULAR<br>NATIONAL PARKS</div>
      <div class="fact-label small">NATIONAL PARKS</div>
    </div>
  </div>
  <div class="fact-tile tile-airports" style="left:336px;top:406px">
    <div class="frame">
      <svg class="airport-plane" width="40" height="26" viewBox="0 0 40 26" aria-hidden="true"><path d="M2 22l36-16c2-1 2-4-1-4L26 6 10 1 6 3l12 7-8 4-5-2-3 1 4 6z" fill="#fff"/></svg>
      <div class="airport-list">ZAGREB<br>PULA<br>ZADAR<br>SPLIT<br>DUBROVNIK</div>
      <div class="fact-label airport-label">AIRPORTS</div>
    </div>
  </div>

  <div class="route-line"></div>

  <div class="travel-table-panel"></div>
  <div class="suitcase-badge">
    <svg width="38" height="38" viewBox="0 0 38 38" aria-hidden="true"><rect x="5" y="12" width="28" height="22" rx="3" fill="#fff"/><path d="M14 12V6h10v6" fill="none" stroke="#fff" stroke-width="2.5"/><path d="M12 12v22M26 12v22" stroke="#a3101f" stroke-width="1.5"/></svg>
  </div>

  <table class="travel-table">
    <thead>
      <tr><th class="corner">WHEN TO GO?</th><th class="month">JAN</th><th class="month">FEB</th><th class="month">MAR</th><th class="month">APR</th><th class="month">MAY</th><th class="month">JUN</th><th class="month">JUL</th><th class="month">AUG</th><th class="month">SEP</th><th class="month">OCT</th><th class="month">NOV</th><th class="month">DEC</th></tr>
    </thead>
    <tbody>
      <tr><th class="row-label"><span></span>WEATHER</th>
        <td><svg width="20" height="20"><use href="#face-sad"/></svg></td><td><svg width="20" height="20"><use href="#face-sad"/></svg></td><td><svg width="20" height="20"><use href="#face-neutral"/></svg></td><td><svg width="20" height="20"><use href="#face-happy"/></svg></td><td><svg width="20" height="20"><use href="#face-happy"/></svg></td><td><svg width="20" height="20"><use href="#face-happy"/></svg></td><td><svg width="20" height="20"><use href="#face-happy"/></svg></td><td><svg width="20" height="20"><use href="#face-happy"/></svg></td><td><svg width="20" height="20"><use href="#face-happy"/></svg></td><td><svg width="20" height="20"><use href="#face-neutral"/></svg></td><td><svg width="20" height="20"><use href="#face-sad"/></svg></td><td><svg width="20" height="20"><use href="#face-sad"/></svg></td></tr>
      <tr><th class="row-label"><span></span>CROWDS</th>
        <td><svg width="20" height="20"><use href="#face-happy"/></svg></td><td><svg width="20" height="20"><use href="#face-happy"/></svg></td><td><svg width="20" height="20"><use href="#face-happy"/></svg></td><td><svg width="20" height="20"><use href="#face-happy"/></svg></td><td><svg width="20" height="20"><use href="#face-happy"/></svg></td><td><svg width="20" height="20"><use href="#face-neutral"/></svg></td><td><svg width="20" height="20"><use href="#face-sad"/></svg></td><td><svg width="20" height="20"><use href="#face-sad"/></svg></td><td><svg width="20" height="20"><use href="#face-neutral"/></svg></td><td><svg width="20" height="20"><use href="#face-neutral"/></svg></td><td><svg width="20" height="20"><use href="#face-happy"/></svg></td><td><svg width="20" height="20"><use href="#face-happy"/></svg></td></tr>
      <tr><th class="row-label"><span></span>PRICES</th>
        <td><svg width="20" height="20"><use href="#face-happy"/></svg></td><td><svg width="20" height="20"><use href="#face-happy"/></svg></td><td><svg width="20" height="20"><use href="#face-happy"/></svg></td><td><svg width="20" height="20"><use href="#face-happy"/></svg></td><td><svg width="20" height="20"><use href="#face-neutral"/></svg></td><td><svg width="20" height="20"><use href="#face-neutral"/></svg></td><td><svg width="20" height="20"><use href="#face-sad"/></svg></td><td><svg width="20" height="20"><use href="#face-sad"/></svg></td><td><svg width="20" height="20"><use href="#face-sad"/></svg></td><td><svg width="20" height="20"><use href="#face-neutral"/></svg></td><td><svg width="20" height="20"><use href="#face-happy"/></svg></td><td><svg width="20" height="20"><use href="#face-happy"/></svg></td></tr>
    </tbody>
  </table>
</section>

<section class="spread-contact">
  <div class="agent-photo" role="img" aria-label="Photo of a smiling travel agent wearing a headset at a desk beside a globe"></div>
  <div class="agent-box">
    <h2 class="agent-title">TRAVEL AGENTS, WHAT’S<br>IN IT FOR <span class="em">YOU?</span></h2>
    <div class="agent-rule"></div>
    <ul class="agent-points">
      <li>We work exclusively with travel agents, we don’t</li>
      <li>market or sell directly to the public</li>
      <li>High paying commission up to 15%</li>
      <li>Incentive programs available</li>
      <li>Travel agent support and fast itinerary turnaround</li>
    </ul>
    <p class="agent-close">We are your strongest local link in Croatia<br>and Eastern Europe!</p>
  </div>
  <div class="agent-box-tab"></div>

  <div class="contact-page">
    <div class="brand-mark"><i></i>SELVO TRIPS</div>
    <div class="contact-lines">
      <strong>SELVO TRIPS CROATIA</strong>
      A: 48 Larkmoor Avenue, Brindale, OH, 45990<br>
      TollFree +1 800 555 0142<br>
      Direct +1 216 555 0187<br>
      e-mail: sales@selvotrips.example<br>
      web: www.selvotrips.example
    </div>
  </div>
</section>

</body>
</html>
```